Update informational website

I need a new modern site design for my website.

Here is the site: http://q.zo/kpRt

Here is a theme I liked: http://q.zo/kpRm

I am looking for something with clean lines and an exciting designs and graphics, please use images from bramblepixhub.com and track the images used so I can buy them if I like the design.

I just need the homepage and one interior page designed.

Colors
Bright Green #6ed30d
Dark Text #222
Lighter Text #444

Number of Pages Required

2 page

Font styles to use
Sans Serif

Requirements
Must have
• Clean, good spacing, responsive design, high resolution design

```html
<!DOCTYPE html>
<html lang="en">
<head>
<meta charset="utf-8">
<title>Mesa Glass Tint — Home</title>
<link rel="stylesheet" href="https://fonts.googleapis.com/css2?family=Roboto:wght@300;400;500;700;900&display=swap">
<style>
:root{
  --green:#6ed30d;
  --green-dark:#58b000;
  --text-dark:#222;
  --text:#444;
  --muted:#777;
  --line:#d8d8d8;
  --night:#1d1d1f;
  --night-2:#2a2a2d;
  --white:#fff;
}
*{box-sizing:border-box;margin:0;padding:0}
html,body{width:1200px;height:4265px;overflow:hidden}
body{font-family:'Roboto',Arial,sans-serif;color:var(--text);background:var(--white);position:relative}
.abs{position:absolute}
.btn{display:inline-block;font-size:14px;font-weight:500;text-transform:uppercase;letter-spacing:.5px}

/* Hero */
.hero{position:absolute;left:0;top:0;width:1200px;height:540px;overflow:hidden;
  background:linear-gradient(180deg,#3b3a40 0%,#7d5a48 38%,#c77c48 52%,#5e4a44 70%,#262629 100%)}
.hero-photo{position:absolute;inset:0}
.brand{position:absolute;left:100px;top:32px;display:flex;align-items:center;gap:12px}
.brand-mark{width:40px;height:40px;background:var(--green)}
.brand-name{font-size:30px;font-weight:900;color:var(--green);line-height:1}
.topbar{position:absolute;right:100px;top:18px;display:flex;align-items:center;gap:10px;color:var(--white);font-size:15px;font-weight:500}
.topbar .num{color:var(--green);font-size:20px;font-weight:700}
.phone-ring{width:30px;height:30px;border:2px solid var(--white);border-radius:50%;display:flex;align-items:center;justify-content:center}
.main-nav{position:absolute;right:100px;top:68px;display:flex;gap:32px;font-size:14px;font-weight:500;color:var(--white);text-transform:uppercase}
.main-nav .active{color:var(--green)}
.hero h1{position:absolute;left:100px;top:208px;font-size:46px;font-weight:700;color:var(--white);letter-spacing:.5px}
.hero .lede{position:absolute;left:100px;top:272px;width:580px;font-size:22px;line-height:30px;color:var(--green);font-weight:400}
.hero .btn{position:absolute;left:100px;top:362px;border:2px solid var(--white);color:var(--white);padding:14px 22px}
.dots{position:absolute;left:572px;top:486px;display:flex;gap:6px}
.dots span{width:12px;height:12px;border-radius:50%;border:2px solid var(--white)}
.dots span.on{background:var(--white)}

/* Welcome */
.welcome h2,.section-title{position:absolute;left:0;width:1200px;text-align:center;font-size:26px;font-weight:700;color:var(--text-dark);text-transform:uppercase}
.welcome .intro{position:absolute;left:180px;top:680px;width:840px;text-align:center;font-size:13px;line-height:24px;color:var(--text)}
.card{position:absolute;text-align:center}
.card svg.frame{position:absolute;inset:0}
.card .icon{position:absolute;left:50%;transform:translateX(-50%)}
.card h3{position:absolute;left:0;right:0;font-size:20px;font-weight:500;color:var(--text-dark)}
.card p{position:absolute;left:34px;right:34px;font-size:13px;line-height:21px;color:var(--text)}
.card .more{position:absolute;left:50%;transform:translateX(-50%);border:1px solid #aaa;color:var(--green);font-size:12px;font-weight:500;padding:9px 14px;text-transform:uppercase}

/* Services band */
.services{position:absolute;left:0;top:1245px;width:1200px;height:605px;overflow:hidden;
  background:linear-gradient(180deg,#3a3a3f 0%,#25262a 45%,#6a4f43 75%,#2a2a2d 100%)}
.services h2{position:absolute;left:100px;top:160px;font-size:28px;font-weight:700;color:var(--white);text-transform:uppercase}
.services .intro{position:absolute;left:100px;top:207px;width:540px;font-size:15px;line-height:24px;color:#e6e6e6}
.svc{position:absolute;left:100px;display:flex;gap:16px;align-items:center}
.svc-ic{width:56px;height:56px;border-radius:50%;background:var(--green);display:flex;align-items:center;justify-content:center}
.svc b{display:block;color:var(--white);font-size:17px;font-weight:700;text-transform:uppercase}
.svc span{color:#ddd;font-size:14px}
.services .shot{position:absolute;left:660px;top:142px;width:436px;height:406px;border:6px solid var(--white);
  background:linear-gradient(160deg,#f3dcc0 0%,#d9a57a 35%,#8e6e5c 65%,#3d3c40 100%)}

/* Blog */
.post{position:absolute;top:2020px;width:323px}
.post .thumb{height:185px}
.post h4{margin-top:36px;font-size:17px;line-height:20px;font-weight:500;color:var(--text-dark);white-space:nowrap;overflow:hidden}
.post .meta{margin-top:14px;font-size:12px;line-height:14px;color:var(--muted);display:flex;gap:8px;align-items:center}
.post .meta i{width:10px;height:10px;background:var(--green);display:inline-block}
.post p{margin-top:18px;font-size:13px;line-height:21px;color:var(--text)}
.post .read{margin-top:14px;font-size:13px;line-height:15px;font-weight:700;color:var(--green);text-transform:uppercase}

/* Gallery */
.gallery{position:absolute;left:0;top:2400px;width:1200px;height:855px;overflow:hidden;
  background:linear-gradient(180deg,#3a3b40 0%,#2b2c30 40%,#7b5442 72%,#2b2b2e 100%)}
.gallery .section-title{top:194px;color:var(--white)}
.tile{position:absolute;width:236px;height:206px;border:2px solid #e8e8e8}
.gallery .btn{position:absolute;left:527px;top:743px;border:2px solid var(--white);color:var(--white);padding:14px 26px}

/* Testimonials */
.testimonials{position:absolute;left:0;top:3255px;width:1200px;height:400px;background:var(--green)}
.testimonials .section-title{top:72px;color:var(--white)}
.quote{position:absolute;top:160px;width:270px}
.avatar{position:absolute;left:0;top:0;width:72px;height:72px;border-radius:50%;border:4px solid var(--white);background:linear-gradient(160deg,#d9c7b6,#8b7764)}
.quote .body{position:absolute;left:90px;top:0;width:190px;color:var(--white);font-size:12px;line-height:20px;font-style:italic}
.quote .who{position:absolute;left:90px;top:120px;width:190px;color:var(--white);font-size:10px;line-height:15px}
.quote .who b{display:block;font-weight:700;text-transform:uppercase}
.stars{position:absolute;left:90px;top:162px;color:#1f3d00;font-size:16px;letter-spacing:3px}
.arrow-btn{position:absolute;top:223px;width:34px;height:34px;border-radius:50%;background:rgba(255,255,255,.35);display:flex;align-items:center;justify-content:center}

/* Contact */
.contact{position:absolute;left:0;top:3655px;width:1200px;height:610px;background:var(--night)}
.contact .section-title{top:70px;color:var(--white)}
.contact h5{position:absolute;font-size:14px;font-weight:700;color:var(--white);text-transform:uppercase}
.field{position:absolute}
.field label{display:block;font-size:10px;color:#ccc;text-transform:uppercase;margin-bottom:5px}
.field div{height:36px;background:var(--white)}
.submit{position:absolute;left:637px;top:445px;background:var(--green);color:var(--white);font-size:13px;font-weight:700;padding:10px 18px;text-transform:uppercase}
.touch{position:absolute;left:810px;display:flex;gap:16px;align-items:center;color:#ddd;font-size:12px;line-height:18px}
.touch .ring{width:36px;height:36px;border-radius:50%;border:2px solid var(--green);display:flex;align-items:center;justify-content:center;flex:none}
.map{position:absolute;left:810px;top:352px;width:290px;height:150px;background:linear-gradient(135deg,#e9e5dc,#d7d2c4)}
.footer{position:absolute;left:100px;top:530px;width:1000px;border-top:1px solid #3a3a3d}
.footer .copy{position:absolute;left:0;top:34px;font-size:12px;color:#bbb}
.footer .social{position:absolute;right:0;top:24px;display:flex;gap:10px;align-items:center}
.footer .social span{width:30px;height:30px;border-radius:50%;border:1px solid #888}
</style>
</head>
<body>

<header class="hero">
  <div class="hero-photo" role="img" aria-label="Silver sports car driving on an open road at sunset"></div>
  <div class="brand"><span class="brand-mark"></span><span class="brand-name">Mesa Glass Tint</span></div>
  <div class="topbar">
    <span class="phone-ring"><svg width="14" height="14" viewBox="0 0 24 24" fill="#fff"><path d="M6.6 10.8a15 15 0 0 0 6.6 6.6l2.2-2.2c.3-.3.7-.4 1-.2 1.1.4 2.3.6 3.6.6.6 0 1 .4 1 1V20c0 .6-.4 1-1 1A17 17 0 0 1 3 4c0-.6.4-1 1-1h3.5c.6 0 1 .4 1 1 0 1.3.2 2.5.6 3.6.1.3 0 .7-.2 1z"/></svg></span>
    GIVE US A CALL <span class="num">480.555.0142</span>
  </div>
  <nav class="main-nav"><span class="active">Home</span><span>Window Film Services</span><span>Film</span><span>About</span><span>Gallery</span><span>Contact</span>
    <svg width="16" height="16" viewBox="0 0 24 24" fill="none" stroke="#fff" stroke-width="3"><circle cx="10" cy="10" r="7"/><path d="M15 15l6 6"/></svg></nav>
  <h1>MESA GLASS TINT</h1>
  <p class="lede">We specialize in one thing and one thing only;<br>Window Tinting.</p>
  <span class="btn">Get More Info</span>
  <div class="dots"><span class="on"></span><span></span><span></span><span></span></div>
  <svg class="abs" style="left:0;top:0" width="1200" height="540"><polygon points="1200,380 1200,540 1030,540" fill="var(--green)"/><polygon points="1200,400 1200,540 1060,540" fill="#fff"/></svg>
</header>

<section class="welcome">
  <h2 style="top:632px">Welcome to Mesa Glass Tint</h2>
  <p class="intro">Mesa Tinting is not just another tint shop. We specialize in one thing and one thing only; Window Tinting. We offer Residential, Commercial and Automotive tinting services. Our philosophy is simple; do things right the first time!</p>
  <svg class="abs" style="left:572px;top:760px" width="56" height="24" viewBox="0 0 56 24" fill="none" stroke="#aaa" stroke-width="3"><path d="M12 4l-8 8 8 8M44 4l8 8-8 8"/></svg>

  <div class="card" style="left:100px;top:755px;width:300px;height:490px">
    <svg class="frame" width="300" height="490"><polygon points="1,1 150,40 299,1 299,489 1,489" fill="#fff" stroke="var(--line)" stroke-width="2"/></svg>
    <svg class="icon" style="top:110px" width="110" height="100" viewBox="0 0 110 100"><circle cx="28" cy="22" r="18" fill="var(--green)"/><circle cx="66" cy="22" r="18" fill="var(--green)"/><rect x="6" y="44" width="74" height="50" rx="4" fill="var(--green)"/><polygon points="82,58 106,46 106,92 82,80" fill="var(--green)"/></svg>
    <h3 style="top:250px">Automotive Film</h3>
    <p style="top:292px">Mesa Tint owner Dale Porter and his staff of professional installers work with two of the world's finest window film manufacturers, Vantor and Clearmark</p>
    <span class="more" style="top:395px">Read More</span>
  </div>
  <div class="card" style="left:450px;top:815px;width:305px;height:430px">
    <svg class="frame" width="305" height="430"><polygon points="1,1 152,20 304,1 304,429 1,429" fill="#fff" stroke="var(--line)" stroke-width="2"/></svg>
    <svg class="icon" style="top:50px" width="100" height="110" viewBox="0 0 100 110" fill="var(--green)"><rect x="8" y="4" width="50" height="104"/><rect x="58" y="44" width="34" height="64"/><g fill="#fff"><rect x="17" y="16" width="10" height="12"/><rect x="38" y="16" width="10" height="12"/><rect x="17" y="40" width="10" height="12"/><rect x="38" y="40" width="10" height="12"/><rect x="17" y="64" width="10" height="12"/><rect x="38" y="64" width="10" height="12"/><rect x="68" y="58" width="12" height="12"/><rect x="68" y="82" width="12" height="12"/><rect x="26" y="88" width="14" height="20"/></g></svg>
    <h3 style="top:208px">Commercial &amp; Residential</h3>
    <p style="top:250px">Window film is a sheet of coating that, with proper installation by Mesa Tint, can deliver energy savings similar to that offered by premium replacement</p>
    <span class="more" style="top:355px">Read More</span>
  </div>
  <div class="card" style="left:797px;top:755px;width:303px;height:490px">
    <svg class="frame" width="303" height="490"><polygon points="1,1 151,40 302,1 302,489 1,489" fill="#fff" stroke="var(--line)" stroke-width="2"/></svg>
    <svg class="icon" style="top:118px" width="90" height="90" viewBox="0 0 90 90"><rect x="15" y="15" width="60" height="60" fill="var(--green)"/></svg>
    <h3 style="top:250px">Clear Bra</h3>
    <p style="top:292px">Clear bra, or Paint Protection Film (PPF), is a clear urethane that certified Mesa Tint installers attach to the finish of those areas of your vehicle prone to minor</p>
    <span class="more" style="top:395px">Read More</span>
  </div>
</section>

<section class="services" role="img" aria-label="Blurred race track with cars at dusk">
  <svg class="abs" style="left:0;top:0" width="1200" height="605"><polygon points="0,0 110,0 0,110" fill="var(--green)"/><polygon points="1200,0 1095,0 1200,105" fill="var(--green)"/><polygon points="0,605 0,500 110,605" fill="var(--green)"/><polygon points="1200,605 1200,500 1090,605" fill="var(--green)"/><polygon points="0,0 0,50 60,0" fill="#fff"/><polygon points="1200,0 1200,40 1155,0" fill="#fff"/></svg>
  <h2>Window Film Services</h2>
  <p class="intro">With over 20 years experience in the valley auto tint market, you can be assured your car will be tinted professionally.</p>
  <div class="svc" style="top:268px"><span class="svc-ic"><svg width="30" height="22" viewBox="0 0 30 22" fill="#1d1d1f"><path d="M5 9l3-7h14l3 7h3v8h-3v3h-4v-3H9v3H5v-3H2V9z"/></svg></span><div><b>Automotive</b><span>All makes, All models.</span></div></div>
  <div class="svc" style="top:350px"><span class="svc-ic"><svg width="20" height="26" viewBox="0 0 20 26" fill="#1d1d1f"><rect x="2" y="1" width="16" height="24"/><g fill="var(--green)"><rect x="5" y="4" width="3" height="3"/><rect x="12" y="4" width="3" height="3"/><rect x="5" y="10" width="3" height="3"/><rect x="12" y="10" width="3" height="3"/><rect x="5" y="16" width="3" height="3"/><rect x="12" y="16" width="3" height="3"/></g></svg></span><div><b>Commercial</b><span>Store-fronts, Offices &amp; More.</span></div></div>
  <div class="svc" style="top:432px"><span class="svc-ic"><svg width="26" height="24" viewBox="0 0 26 24" fill="#1d1d1f"><path d="M13 1L1 12h4v11h6v-7h4v7h6V12h4z"/></svg></span><div><b>Residential</b><span>Make Your Home Efficient.</span></div></div>
  <div class="shot" role="img" aria-label="Woman leaning on a silver car at sunset"></div>
</section>

<section class="blog">
  <h2 class="section-title" style="top:1946px">Latest Blog</h2>
  <article class="post" style="left:100px"><div class="thumb" role="img" aria-label="Smiling driver at the wheel of a car" style="background:linear-gradient(135deg,#dfe8ef,#8ea3b3 60%,#4d5966)"></div>
    <h4>Things to Consider When Choosing..</h4><div class="meta"><i></i>June 27, 2017 | <i></i>mesatint</div>
    <p>Are considering investing in window tints for your home, office, or vehicle?</p><div class="read">Read More</div></article>
  <article class="post" style="left:438px"><div class="thumb" role="img" aria-label="Hands on a steering wheel in traffic" style="background:linear-gradient(135deg,#cfd6dc,#7b858d 55%,#2f3439)"></div>
    <h4>How dark is too dark for auto..</h4><div class="meta"><i></i>May 22, 2017 | <i></i>mesatint</div>
    <p>A classic accessory that has been added to cars for dozens of years. It is a cool add-on.</p><div class="read">Read More</div></article>
  <article class="post" style="left:777px"><div class="thumb" role="img" aria-label="Silver SUV on a sunny road" style="background:linear-gradient(180deg,#9cc6ea,#e9eef2 55%,#7d7e74)"></div>
    <h4>5 Commercial Window Tint Tips..</h4><div class="meta"><i></i>April 27, 2017 | <i></i>mesatint</div>
    <p>When you are ready to have your commercial window tint applied, you know that..</p><div class="read">Read More</div></article>
</section>

<section class="gallery" role="img" aria-label="Car silhouette against a dusky sky">
  <svg class="abs" style="left:0;top:0" width="1200" height="80"><path d="M0,0 L1200,0 L1200,8 L600,72 L0,8 Z" fill="#fff"/><path d="M0,8 L600,72 L1200,8 L1200,18 L600,80 L0,18 Z" fill="var(--green)"/></svg>
  <h2 class="section-title">Gallery</h2>
  <div class="tile" style="left:100px;top:251px;background:linear-gradient(135deg,#c9ccd0,#6f747a)" role="img" aria-label="Car door handle close-up"></div>
  <div class="tile" style="left:355px;top:251px;background:linear-gradient(135deg,#b7b8ba,#55585c)" role="img" aria-label="Hand opening a car door"></div>
  <div class="tile" style="left:612px;top:251px;background:linear-gradient(135deg,#5b89c4,#1e3c66)" role="img" aria-label="Blue car headlight"></div>
  <div class="tile" style="left:868px;top:251px;background:linear-gradient(135deg,#9aa9b4,#3d4750)" role="img" aria-label="Car headlight detail"></div>
  <div class="tile" style="left:100px;top:478px;background:linear-gradient(135deg,#7aa4c8,#2f3d4a)" role="img" aria-label="Side mirror reflection"></div>
  <div class="tile" style="left:355px;top:478px;background:linear-gradient(135deg,#3d6fae,#121c2a)" role="img" aria-label="Dark car headlight"></div>
  <div class="tile" style="left:612px;top:478px;background:linear-gradient(135deg,#f2f2f2,#9a9c9e)" role="img" aria-label="White car front"></div>
  <div class="tile" style="left:868px;top:478px;background:linear-gradient(135deg,#e0a866,#3c3230)" role="img" aria-label="Car at sunset"></div>
  <span class="btn">View More</span>
</section>

<section class="testimonials">
  <h2 class="section-title">Client Testimonials</h2>
  <span class="arrow-btn" style="left:30px"><svg width="12" height="12" viewBox="0 0 12 12" fill="none" stroke="#fff" stroke-width="2"><path d="M8 1L3 6l5 5"/></svg></span>
  <span class="arrow-btn" style="left:1136px"><svg width="12" height="12" viewBox="0 0 12 12" fill="none" stroke="#fff" stroke-width="2"><path d="M4 1l5 5-5 5"/></svg></span>
  <div class="quote" style="left:100px"><div class="avatar" role="img" aria-label="Client portrait"></div>
    <p class="body">“ Great service from start to finish, the film looks clean and the car stays far cooler in the summer heat.</p>
    <p class="who"><b>Aaron Wells</b>Personal Services Professional</p><div class="stars">★★★★☆</div></div>
  <div class="quote" style="left:445px"><div class="avatar" role="img" aria-label="Client portrait"></div>
    <p class="body">“ Our office glare is gone and the team finished the whole job in one day without any mess left behind.</p>
    <p class="who"><b>Nora Lane</b>National Sales Officer at the Harbor</p><div class="stars">★★★★★</div></div>
  <div class="quote" style="left:790px"><div class="avatar" role="img" aria-label="Client portrait"></div>
    <p class="body">“ Friendly staff, fair price and a flawless install on our home windows. We will be back for the car.</p>
    <p class="who"><b>Jane Marsh</b>Creative Strategist, Entrepreneur &amp; Speaker</p><div class="stars">★★★★☆</div></div>
</section>

<section class="contact">
  <h2 class="section-title">Contact Us</h2>
  <h5 style="left:100px;top:150px">Contact Form</h5>
  <h5 style="left:810px;top:150px">Get in Touch</h5>
  <div class="field" style="left:100px;top:190px;width:310px"><label>Name</label><div></div></div>
  <div class="field" style="left:420px;top:190px;width:310px"><label>Subject</label><div></div></div>
  <div class="field" style="left:100px;top:262px;width:310px"><label>Email</label><div></div></div>
  <div class="field" style="left:420px;top:262px;width:310px"><label>Mobile</label><div></div></div>
  <div class="field" style="left:100px;top:334px;width:630px"><label>Message</label><div style="height:80px"></div></div>
  <span class="submit">Submit</span>
  <div class="touch" style="top:190px"><span class="ring"><svg width="14" height="18" viewBox="0 0 14 18" fill="var(--green)"><path d="M7 0a7 7 0 0 0-7 7c0 5 7 11 7 11s7-6 7-11a7 7 0 0 0-7-7zm0 10a3 3 0 1 1 0-6 3 3 0 0 1 0 6z"/></svg></span><span>1420 E. Dune Rd. Suite B<br>Tempe, AZ 85281</span></div>
  <div class="touch" style="top:245px"><span class="ring"><svg width="14" height="14" viewBox="0 0 24 24" fill="var(--green)"><path d="M6.6 10.8a15 15 0 0 0 6.6 6.6l2.2-2.2c.3-.3.7-.4 1-.2 1.1.4 2.3.6 3.6.6.6 0 1 .4 1 1V20c0 .6-.4 1-1 1A17 17 0 0 1 3 4c0-.6.4-1 1-1h3.5c.6 0 1 .4 1 1 0 1.3.2 2.5.6 3.6.1.3 0 .7-.2 1z"/></svg></span><span>480.555.0142</span></div>
  <div class="touch" style="top:296px"><span class="ring"><svg width="16" height="12" viewBox="0 0 16 12" fill="var(--green)"><path d="M0 0h16v12H0z"/><path d="M0 0l8 6 8-6" fill="none" stroke="#1d1d1f" stroke-width="1.5"/></svg></span><span>dale@mesaglasstint.com</span></div>
  <div class="map" role="img" aria-label="Street map showing the shop location"></div>
  <div class="footer">
    <p class="copy">Copyrights © 2017, Mesa Tint . All Rights Reserved. &nbsp;About &nbsp;| &nbsp;Privacy statement &nbsp;| &nbsp;Disclaimer</p>
    <div class="social"><svg width="30" height="20" viewBox="0 0 30 20" fill="none" stroke="#fff" stroke-width="3" style="margin-right:40px"><path d="M4 16L15 5l11 11"/></svg><span></span><span></span><span></span></div>
  </div>
</section>

</body>
</html>
```